The Academy for Stewardship in Civic Builds' 2024 Lift Her Up Summit: Spark Venture needs a full page flyer that can be converted to a website header.

Date: February, 16, 2024
Location: Harborline Lodge Meeting Hall, San Marcos, TX

ABOUT THE FORUM

Dedicated to celebrating the entrepreneurial spirit and unwavering determination of women, the Lift Her Up Summit proudly presents, “Spark Venture.” Here, we believe in the power of dreams, the strength of innovation, and the impact of women-led endeavors.

Join us at this dynamic Forum as we explore the world of Passion Projects – those inspiring ventures, including YOURSELF, fueled by creativity, ambition, and a deep-seated love for what we do. Whether you're an seasoned expert, a budding visionary, or simply an enthusiast eager to learn and grow, this Forum is your hub for all things related to the fusion of passion and business.

WHAT TO EXPECT

Inspiring Stories: Immerse yourself in a collection of captivating success stories and personal journeys that highlight the incredible feats achieved through passion-driven initiatives. Learn from remarkable women who turned their dreams into reality and gain insights into their strategies, challenges, and triumphs.

Expert Insights: Discover the art of transforming a passion into a sustainable business model. Our forum gathers experts and thought leaders across the AEC community (and more) to share invaluable advice, practical tips, and proven strategies, guiding you along the exciting journey of pursuing your passion.

Networking Opportunities: Connect with like-minded individuals who share your passion for making a difference. Engage in lively discussions, exchange ideas, and build meaningful relationships with fellow forum participants, potential collaborators, and mentors who can help elevate your Spark Venture.

Interactive Workshops: Participate in hands-on workshops designed to enhance your skills, from refining your business plan to mastering effective marketing techniques. These immersive sessions are tailored to address the unique challenges faced by women in the design and construction industry and will empower you to overcome obstacles with confidence.

Passion Showcase: Elevate your project's visibility by showcasing your Spark Venture to the Forum. Receive feedback, support, and perhaps even connect with individuals who are excited to collaborate and join you on your journey.

Empowerment and Support: Embrace a supportive community that believes in your potential and is committed to fostering an inclusive environment. Share your highs and lows, seek advice, and find encouragement to keep pursuing your passion, no matter the hurdles.

Join Us!

Whether you're taking your first steps toward transforming your passion into a business or are seeking to amplify the impact of your existing venture, or just personal improvement, the Lift Her Up Summit: "Spark Venture" is your gateway to inspiration, knowledge, and connection. Let's come together, celebrate the strength of women-led endeavors, and empower one another to turn our passions into legacies that shape the future.

Target Market(s)

Professionals in the design and construction industry.

Industry/Entity Type

Design and Construction

Requirements
Must have
• A-StCB logo
Nice to have
• Title, Date, Location, Graphics that fit the theme of the the Forum: Spark Venture, and the mission of the organization.
Should not have
• Full description of event should be in the graphic.

```html
<!DOCTYPE html>
<html lang="en">
<head>
<meta charset="utf-8">
<title>Lift Her Up Summit: Spark Venture</title>
<link rel="stylesheet" href="https://fonts.googleapis.com/css2?family=Poppins:ital,wght@0,300;0,400;0,600;0,700;0,800;1,300;1,400&family=Playfair+Display:ital,wght@1,700&display=swap">
<style>
  :root {
    --green: #8db040;
    --green-deep: #7ea236;
    --blue: #3652a0;
    --navy: #34489c;
    --white: #ffffff;
    --ink: #2f2f2f;
    --photo-light: #f3efea;
    --photo-mid: #ddd3ca;
  }
  * { box-sizing: border-box; margin: 0; padding: 0; }
  html, body { width: 927px; height: 1200px; overflow: hidden; background: var(--white); }
  body { font-family: "Poppins", Arial, sans-serif; color: var(--white); }

  .flyer { position: relative; width: 927px; height: 1200px; overflow: hidden; background: var(--green); }

  .backdrop-photo {
    position: absolute; inset: 0 0 72px 0;
    background:
      radial-gradient(ellipse 200px 260px at 180px 360px, rgba(255,255,255,0.07), transparent 70%),
      radial-gradient(ellipse 220px 280px at 760px 300px, rgba(255,255,255,0.08), transparent 70%),
      radial-gradient(ellipse 180px 240px at 420px 260px, rgba(60,90,20,0.10), transparent 70%);
  }

  .shapes { position: absolute; left: 0; top: 0; width: 927px; height: 1200px; }

  .hero-photo {
    position: absolute; left: 455px; top: 214px; width: 472px; height: 914px;
    border-radius: 250px 250px 0 0 / 300px 300px 0 0;
    background: linear-gradient(180deg, var(--photo-mid) 0%, var(--photo-light) 45%, #c9d3e2 100%);
  }

  .brand { position: absolute; left: 640px; top: 50px; display: flex; align-items: center; gap: 12px; }
  .brand-square { width: 26px; height: 26px; background: var(--green); flex-shrink: 0; }
  .brand-name { font-weight: 600; font-size: 16px; line-height: 20px; color: var(--navy); letter-spacing: -0.2px; }

  .headline {
    position: absolute; left: 79px; top: 82px; white-space: nowrap;
    font-weight: 300; font-size: 38px; line-height: 52px; letter-spacing: -0.9px;
  }
  .intro {
    position: absolute; left: 82px; top: 294px; white-space: nowrap;
    font-weight: 300; font-size: 17.2px; line-height: 22px; letter-spacing: -0.3px;
  }
  .intro strong { font-weight: 600; }
  .event-title {
    position: absolute; left: 84px; top: 360px;
    font-family: "Playfair Display", Georgia, serif; font-style: italic; font-weight: 700;
    font-size: 37px; letter-spacing: -0.5px;
  }

  .join-card {
    position: absolute; left: 78px; top: 429px; width: 427px; height: 199px;
    border: 3px solid var(--white); border-bottom: none; border-radius: 16px 16px 0 0; overflow: hidden;
  }
  .join-head { height: 138px; text-align: center; padding-top: 8px; }
  .join-title { font-weight: 800; font-size: 52px; line-height: 56px; letter-spacing: 0.5px; color: var(--white); }
  .join-venue { font-weight: 600; font-size: 26px; line-height: 32px; letter-spacing: -1.2px; color: var(--navy); }
  .join-date {
    height: 61px; background: var(--white); text-align: center;
    font-weight: 700; font-size: 31px; line-height: 58px; letter-spacing: -1px; color: var(--green);
  }

  .pitch {
    position: absolute; left: 77px; top: 641px; white-space: nowrap;
    font-weight: 300; font-size: 17.3px; line-height: 21.8px; letter-spacing: -0.35px;
  }
  .expect-heading {
    position: absolute; left: 75px; top: 810px;
    font-weight: 800; font-size: 21.5px; letter-spacing: -0.3px;
  }
  .expect-list { position: absolute; left: 80px; top: 845px; list-style: none; }
  .expect-item { display: flex; align-items: center; height: 40.5px; }
  .expect-icon {
    width: 34px; height: 34px; border-radius: 50%; background: var(--green);
    display: flex; align-items: center; justify-content: center; flex-shrink: 0;
  }
  .expect-icon svg { width: 20px; height: 20px; }
  .expect-label { margin-left: 8px; font-style: italic; font-weight: 300; font-size: 19.5px; letter-spacing: -0.3px; }

  .footer {
    position: absolute; left: 0; top: 1128px; width: 927px; height: 72px; background: var(--white);
    display: flex; align-items: center; padding-left: 85px; font-size: 20.5px; color: var(--ink); font-weight: 300;
  }
  .footer-label { color: var(--green); font-weight: 600; margin-right: 18px; letter-spacing: -0.4px; }
  .footer-sep { margin: 0 16px; }
</style>
</head>
<body>
<main class="flyer">
  <div class="backdrop-photo" role="img" aria-label="Faded green-tinted photo of women celebrating together"></div>

  <svg class="shapes" viewBox="0 0 927 1200" aria-hidden="true">
    <path d="M0 555 C150 592 300 640 520 612 L927 565 L927 1128 L0 1128 Z" fill="var(--blue)"/>
    <path d="M456 0 C540 40 585 110 650 148 C720 186 800 172 927 150 L927 0 Z" fill="var(--white)"/>
  </svg>

  <div class="hero-photo" role="img" aria-label="Photo of a smiling professional woman in glasses and a white shirt holding a tablet"></div>

  <div class="brand">
    <span class="brand-square"></span>
    <span class="brand-name">Academy for Stewardship<br>in Civic Builds</span>
  </div>

  <h1 class="headline">We believe in the power<br>of dreams, the strength of<br>innovation, and the impact<br>of women-led endeavors.</h1>

  <p class="intro">Dedicated to celebrating the entrepreneurial spirit and<br>unwavering determination of women, the <strong>Lift Her Up</strong><br><strong>Summit</strong> proudly presents:</p>
  <p class="event-title">“Spark Venture”</p>

  <section class="join-card">
    <div class="join-head">
      <div class="join-title">JOIN US!</div>
      <div class="join-venue">Harborline Lodge Meeting<br>Hall, San Marcos, TX</div>
    </div>
    <div class="join-date">FEBRUARY 16, 2024</div>
  </section>

  <p class="pitch">Whether you're taking your first steps toward<br>transforming your passion into a business or<br>are seeking to amplify the impact of<br>your existing venture, or just personal<br>improvement, the Lift Her Up<br>Summit: "Spark Venture" is your gateway<br>to inspiration, knowledge, and connection.</p>

  <h2 class="expect-heading">WHAT TO EXPECT:</h2>
  <ul class="expect-list">
    <li class="expect-item">
      <span class="expect-icon"><svg viewBox="0 0 20 20" fill="#fff"><path d="M9 2 L10.6 7.4 L16 9 L10.6 10.6 L9 16 L7.4 10.6 L2 9 L7.4 7.4 Z"/><path d="M15.5 12 L16.2 14 L18 14.6 L16.2 15.3 L15.5 17.5 L14.8 15.3 L13 14.6 L14.8 14 Z"/></svg></span>
      <span class="expect-label">Inspiring Stories</span>
    </li>
    <li class="expect-item">
      <span class="expect-icon"><svg viewBox="0 0 20 20" fill="none" stroke="#fff" stroke-width="2.2" stroke-linecap="round"><circle cx="8" cy="8" r="5"/><path d="M12 12 L17 17"/></svg></span>
      <span class="expect-label">Expert Insights</span>
    </li>
    <li class="expect-item">
      <span class="expect-icon"><svg viewBox="0 0 20 20" fill="#fff" stroke="#fff" stroke-width="1.2"><path d="M5 5 L10 10 L15 5 M10 10 L5 15 M10 10 L15 15" fill="none"/><circle cx="10" cy="10" r="2.3"/><circle cx="4.5" cy="4.5" r="2"/><circle cx="15.5" cy="4.5" r="2"/><circle cx="4.5" cy="15.5" r="2"/><circle cx="15.5" cy="15.5" r="2"/></svg></span>
      <span class="expect-label">Networking Opportunities</span>
    </li>
    <li class="expect-item">
      <span class="expect-icon"><svg viewBox="0 0 20 20" fill="none" stroke="#fff" stroke-width="1.5" stroke-linecap="round"><path d="M7 13 C4 11 4 4 10 3.5 C16 4 16 11 13 13 L13 15 L7 15 Z"/><path d="M8 17.5 H12"/><circle cx="10" cy="9" r="2"/></svg></span>
      <span class="expect-label">Interactive Workshops</span>
    </li>
    <li class="expect-item">
      <span class="expect-icon"><svg viewBox="0 0 20 20" fill="none" stroke="#fff" stroke-width="1.6" stroke-linejoin="round"><path d="M10 2 C12 6 15 8 15 12 A5 5 0 0 1 5 12 C5 9 7 8 7.5 6 C8.5 8 9 8.5 10 9 C10.5 7 10.5 5 10 2 Z"/></svg></span>
      <span class="expect-label">Passion Showcase</span>
    </li>
    <li class="expect-item">
      <span class="expect-icon"><svg viewBox="0 0 20 20" fill="none" stroke="#fff" stroke-width="1.5" stroke-linejoin="round"><rect x="5" y="6" width="10" height="7" rx="2"/><path d="M8 6 V13 M11 6 V13 M7 13 L7 18 H13 L13 13"/></svg></span>
      <span class="expect-label">Empowerment and Support</span>
    </li>
  </ul>

  <footer class="footer">
    <span class="footer-label">For more details:</span>
    <span>[insert contact details here]</span>
    <span class="footer-sep">|</span>
    <span>[insert wesite details here]</span>
  </footer>
</main>
</body>
</html>
```